Clinical pathology box packaging and brand design

I have a box template I wanted to design for a new medical education company. The box template(top and bottom) and the illustration to use will be included and directions as to what to write on the box. The illustration should fit on the largest surface area on the side of the box.
This is the first box in our line of products and we need to have students to look at as something they can buy and have fun while learning a very difficult subject.
Updates

Need extra days to review

Target Market(s)

Medical students is my primary market. Then Nurses, physician assistants

Requirements
Must have
• https://files.plonkriver.net/doc/7Kq2Vx9TzR4mWb8NcJ3fLs6PyD1hGu5aE0oXiY2eBt/view?mode=share

```html
<!DOCTYPE html>
<html lang="en">
<head>
<meta charset="utf-8">
<title>Lumenta – Clinical Reasoning box dielines</title>
<link rel="stylesheet" href="https://fonts.googleapis.com/css2?family=Open+Sans:wght@400;600;700;800&display=swap">
<style>
  :root {
    --canvas: #ffffff;
    --brand-red: #e8503a;
    --flap: #f7f7f7;
    --label: #ffffff;
    --ink: #3c4a50;
    --teal: #27b1a3;
    --cutline: #e2323d;
  }
  html, body {
    margin: 0;
    padding: 0;
    width: 770px;
    height: 1200px;
    overflow: hidden;
    background: var(--canvas);
    font-family: "Open Sans", Arial, sans-serif;
  }
  .sheet {
    position: relative;
    width: 770px;
    height: 1200px;
  }
  .dielines {
    position: absolute;
    left: 0;
    top: 312px;
    width: 770px;
    height: 575px;
  }
  .cut { stroke: var(--cutline); stroke-width: 1.2; }
  .flap { fill: var(--flap); }
  .panel-red { fill: url(#redWash); }
  .panel-grey { fill: url(#greyWash); }
  .label { fill: var(--label); }
  .brand-dot { fill: none; stroke: var(--teal); stroke-width: 4; }
  .brand-dot.on-red { stroke: #ffffff; }
  .brand-name { font-weight: 600; fill: var(--ink); }
  .brand-name.on-red { fill: #ffffff; }
  .title-dark { font-weight: 800; fill: var(--ink); }
  .title-red { font-weight: 800; fill: var(--brand-red); }
  .subtitle { font-weight: 400; fill: var(--ink); }
  .tagline { font-weight: 400; fill: var(--ink); }
  .count { font-weight: 700; fill: var(--ink); }
  .count-num { fill: var(--teal); }
  .scene-fill { fill: url(#sceneWash); }
</style>
</head>
<body>
<main class="sheet">
  <svg class="dielines" viewBox="40 1260 1460 1090" xmlns="http://www.w3.org/2000/svg" font-family="Open Sans, Arial, sans-serif">
    <defs>
      <linearGradient id="redWash" x1="0" y1="0" x2="1" y2="1">
        <stop offset="0" stop-color="#ec5a42"/>
        <stop offset="1" stop-color="#dc4530"/>
      </linearGradient>
      <linearGradient id="greyWash" x1="0" y1="0" x2="1" y2="1">
        <stop offset="0" stop-color="#f3f3f3"/>
        <stop offset="1" stop-color="#e3e3e3"/>
      </linearGradient>
      <linearGradient id="sceneWash" x1="0" y1="0" x2="0" y2="1">
        <stop offset="0" stop-color="#e5533c"/>
        <stop offset="0.6" stop-color="#8fa6c2"/>
        <stop offset="1" stop-color="#dfe6ee"/>
      </linearGradient>
    </defs>

    <!-- LID -->
    <g class="lid">
      <rect class="flap cut" x="185" y="1432" width="262" height="36"/>
      <rect class="flap cut" x="185" y="1925" width="262" height="37"/>
      <rect class="flap cut" x="55" y="1562" width="38" height="270"/>
      <rect class="flap cut" x="538" y="1562" width="37" height="270"/>
      <polygon class="flap cut" points="93,1562 100,1525 185,1525 185,1562"/>
      <polygon class="flap cut" points="93,1832 185,1832 185,1868 100,1868"/>
      <polygon class="flap cut" points="447,1562 447,1525 531,1525 538,1562"/>
      <polygon class="flap cut" points="447,1832 538,1832 531,1868 447,1868"/>
      <rect class="panel-grey cut" x="93" y="1562" width="92" height="270" role="img" aria-label="Soft grey cell pattern"/>
      <rect class="panel-grey cut" x="447" y="1562" width="91" height="270" role="img" aria-label="Soft grey cell pattern"/>
      <rect class="panel-grey cut" x="185" y="1562" width="262" height="270" role="img" aria-label="Soft grey cell pattern"/>
      <rect class="panel-red cut" x="185" y="1468" width="262" height="94" role="img" aria-label="Red cell pattern"/>
      <rect class="panel-red cut" x="185" y="1832" width="262" height="93" role="img" aria-label="Red cell pattern"/>

      <circle class="brand-dot" cx="316" cy="1660" r="28"/>
      <text class="brand-name" x="316" y="1745" font-size="38" text-anchor="middle">Lumenta</text>

      <g transform="rotate(180 315 1508)">
        <rect class="label" x="226" y="1470" width="178" height="77" rx="6"/>
        <text class="title-dark" x="315" y="1500" font-size="13" text-anchor="middle">CLINICAL REASONING</text>
        <text class="subtitle" x="315" y="1513" font-size="6.5" text-anchor="middle">A CASE-BASED LEARNING METHOD</text>
        <text class="count" x="315" y="1535" font-size="9" text-anchor="middle"><tspan class="count-num">240</tspan> Study Cards</text>
      </g>

      <rect class="label" x="226" y="1851" width="178" height="71" rx="6"/>
      <text class="title-dark" x="315" y="1877" font-size="13" text-anchor="middle">CLINICAL REASONING</text>
      <text class="subtitle" x="315" y="1889" font-size="6.5" text-anchor="middle">A CASE-BASED LEARNING METHOD</text>
      <text class="count" x="315" y="1912" font-size="9" text-anchor="middle"><tspan class="count-num">240</tspan> Study Cards</text>
    </g>

    <!-- BASE -->
    <g class="base">
      <rect class="flap cut" x="914" y="1273" width="270" height="39"/>
      <rect class="flap cut" x="914" y="2090" width="270" height="35"/>
      <rect class="flap cut" x="619" y="1568" width="37" height="264"/>
      <rect class="flap cut" x="1443" y="1568" width="38" height="264"/>
      <polygon class="flap cut" points="914,1312 876,1320 876,1568 914,1568"/>
      <polygon class="flap cut" points="1184,1312 1222,1320 1222,1568 1184,1568"/>
      <polygon class="flap cut" points="914,1832 876,1832 876,2082 914,2090"/>
      <polygon class="flap cut" points="1184,1832 1222,1832 1222,2082 1184,2090"/>

      <rect class="panel-grey cut" x="656" y="1568" width="258" height="264" role="img" aria-label="Soft grey cell pattern"/>
      <rect class="panel-grey cut" x="914" y="1568" width="270" height="264" role="img" aria-label="Soft grey cell pattern"/>
      <rect class="panel-grey cut" x="1184" y="1568" width="259" height="264" role="img" aria-label="Soft grey cell pattern"/>
      <rect class="panel-red cut" x="914" y="1312" width="270" height="256" role="img" aria-label="Red cell pattern"/>
      <rect class="panel-red cut" x="914" y="1832" width="270" height="258"/>

      <rect class="label" x="960" y="1312" width="178" height="208" rx="8"/>
      <circle class="brand-dot" cx="1049" cy="1346" r="20"/>
      <text class="brand-name" x="1049" y="1394" font-size="24" text-anchor="middle">Lumenta</text>
      <text class="title-dark" x="1049" y="1432" font-size="19" text-anchor="middle">CLINICAL</text>
      <text class="title-red" x="1049" y="1451" font-size="19" text-anchor="middle">REASONING</text>
      <text class="subtitle" x="1049" y="1463" font-size="6.5" text-anchor="middle">A CASE-BASED LEARNING METHOD</text>
      <text class="tagline" x="1049" y="1496" font-size="7" text-anchor="middle">Train with simulated cases</text>
      <text class="count" x="1049" y="1509" font-size="9" text-anchor="middle"><tspan class="count-num">240</tspan> Study Cards</text>

      <rect class="scene-fill" x="915" y="1895" width="268" height="194" role="img" aria-label="Illustration of a nurse and doctor attending a patient in a hospital bed"/>
      <circle class="brand-dot on-red" cx="1049" cy="1866" r="20"/>
      <text class="brand-name on-red" x="1049" y="1918" font-size="24" text-anchor="middle">Lumenta</text>

      <g transform="rotate(-90 785 1700)">
        <circle class="brand-dot" cx="785" cy="1616" r="18"/>
        <text class="brand-name" x="785" y="1664" font-size="22" text-anchor="middle">Lumenta</text>
        <text class="title-dark" x="785" y="1690" font-size="15" text-anchor="middle">CLINICAL</text>
        <text class="title-red" x="785" y="1706" font-size="15" text-anchor="middle">REASONING</text>
        <text class="subtitle" x="785" y="1720" font-size="6" text-anchor="middle">A CASE-BASED LEARNING METHOD</text>
        <text class="count" x="785" y="1791" font-size="8.5" text-anchor="middle"><tspan class="count-num">240</tspan> Study Cards</text>
      </g>

      <g transform="rotate(90 1313 1700)">
        <circle class="brand-dot" cx="1313" cy="1616" r="18"/>
        <text class="brand-name" x="1313" y="1664" font-size="22" text-anchor="middle">Lumenta</text>
        <text class="title-dark" x="1313" y="1690" font-size="15" text-anchor="middle">CLINICAL</text>
        <text class="title-red" x="1313" y="1706" font-size="15" text-anchor="middle">REASONING</text>
        <text class="subtitle" x="1313" y="1720" font-size="6" text-anchor="middle">A CASE-BASED LEARNING METHOD</text>
        <text class="count" x="1313" y="1791" font-size="8.5" text-anchor="middle"><tspan class="count-num">240</tspan> Study Cards</text>
      </g>
    </g>

    <!-- INNER SLEEVE STRIP -->
    <rect class="flap cut" x="197" y="2140" width="1114" height="190"/>
  </svg>
</main>
</body>
</html>
```